Security Camera Sign

14” high x 11” wide Color: Blue, Yellow, Black and white

Make the sign vertical
Replace red with blue
WARNING: Black over yellow
These premises are protected by Closed Circuit Television: On white
Images are recorded for crime prevention and public safety. Unauthorized access, theft or vandalism will result in prosecution: On Blue

Target Market(s)

Outdoor commercial building

Industry/Entity Type

Security

Requirements
Nice to have
• I would like the sign stand out. If you need more colors? Thanks Ok

```html
<!DOCTYPE html>
<html lang="en">
<head>
<meta charset="utf-8">
<title>Security Camera Sign</title>
<link rel="stylesheet" href="https://fonts.googleapis.com/css2?family=Open+Sans:wght@700;800&display=swap">
<style>
  :root {
    --backdrop: #e6e8ec;
    --sign-blue: #1b1b8f;
    --sign-edge: #0c0c3a;
    --warning-yellow: #eefc22;
    --ink-black: #0b0b0b;
    --panel-white: #eef3f8;
    --text-white: #ffffff;
    --camera-light: #f7f9fb;
    --camera-mid: #c9ced6;
  }
  html, body {
    margin: 0;
    padding: 0;
    width: 918px;
    height: 1200px;
    overflow: hidden;
    background: var(--backdrop);
  }
  .canvas {
    display: block;
    width: 918px;
    height: 1200px;
  }
  .sign-body { fill: var(--sign-blue); stroke: var(--sign-edge); stroke-width: 4; }
  .warning-band { fill: var(--warning-yellow); stroke: var(--ink-black); stroke-width: 5; }
  .info-panel { fill: var(--panel-white); }
  .warning-title {
    font-family: "Open Sans", Arial, sans-serif;
    font-weight: 800;
    font-size: 148px;
    fill: var(--ink-black);
  }
  .cctv-notice {
    font-family: "Open Sans", Arial, sans-serif;
    font-weight: 700;
    font-size: 68px;
    fill: var(--ink-black);
    text-anchor: middle;
  }
  .legal-notice {
    font-family: "Open Sans", Arial, sans-serif;
    font-weight: 700;
    font-size: 43px;
    fill: var(--text-white);
    text-anchor: middle;
  }
</style>
</head>
<body>
<svg class="canvas" viewBox="0 0 918 1200" xmlns="http://www.w3.org/2000/svg">
  <defs>
    <linearGradient id="camera-tone" x1="0" y1="0" x2="1" y2="1">
      <stop offset="0" stop-color="#f7f9fb"/>
      <stop offset="1" stop-color="#c9ced6"/>
    </linearGradient>
  </defs>

  <g class="security-sign">
    <rect class="sign-body" x="34" y="52" width="844" height="1094" rx="48"/>

    <rect class="warning-band" x="74" y="94" width="762" height="182" rx="14"/>
    <text class="warning-title" x="104" y="243" textLength="702" lengthAdjust="spacingAndGlyphs">WARNING</text>

    <rect class="info-panel" x="38" y="314" width="836" height="548"/>

    <rect class="camera-illustration" x="456" y="376" width="384" height="444" rx="8"
          fill="url(#camera-tone)" role="img" aria-label="Line illustration of a wall-mounted security camera"/>

    <g class="cctv-notice-block">
      <text class="cctv-notice" x="256" y="408" textLength="186" lengthAdjust="spacingAndGlyphs">THESE</text>
      <text class="cctv-notice" x="256" y="478" textLength="296" lengthAdjust="spacingAndGlyphs">PREMISES</text>
      <text class="cctv-notice" x="256" y="546" textLength="118" lengthAdjust="spacingAndGlyphs">ARE</text>
      <text class="cctv-notice" x="256" y="613" textLength="354" lengthAdjust="spacingAndGlyphs">PROTECTED</text>
      <text class="cctv-notice" x="256" y="680" textLength="330" lengthAdjust="spacingAndGlyphs">BY CLOSED</text>
      <text class="cctv-notice" x="256" y="749" textLength="238" lengthAdjust="spacingAndGlyphs">CIRCUIT</text>
      <text class="cctv-notice" x="256" y="816" textLength="362" lengthAdjust="spacingAndGlyphs">TELEVISION</text>
    </g>

    <g class="legal-notice-block">
      <text class="legal-notice" x="456" y="932" textLength="752" lengthAdjust="spacingAndGlyphs">IMAGES ARE RECORDED FOR CRIME</text>
      <text class="legal-notice" x="456" y="976" textLength="732" lengthAdjust="spacingAndGlyphs">PREVENTION AND PUBLIC SAFETY.</text>
      <text class="legal-notice" x="456" y="1020" textLength="534" lengthAdjust="spacingAndGlyphs">UNAUTHORIZED ACCESS,</text>
      <text class="legal-notice" x="456" y="1064" textLength="590" lengthAdjust="spacingAndGlyphs">THEFT OR VANDALISM WILL</text>
      <text class="legal-notice" x="456" y="1108" textLength="532" lengthAdjust="spacingAndGlyphs">RESULT IN PROSECUTION</text>
    </g>
  </g>
</svg>
</body>
</html>
```